Business Cards/Letterhead for Electrical Contractor
Electrical Contractor
Business Cards/Letterhead for Electrical Contractor - Construction
Creative Brief
Use same font as used in my logo
A combination may be used
Modern
Derek Stallworth
President
48306 Calloway Avenue Fenmoor City, ST 00000
derek@quorvantpower.example

```html
<!DOCTYPE html>
<html lang="en">
<head>
<meta charset="utf-8">
<title>Quorvant Power Stationery</title>
<link href="https://fonts.googleapis.com/css2?family=Montserrat:wght@400;600;700&display=swap" rel="stylesheet">
<style>
:root{
  --stage:#2b2d30;
  --paper:#ffffff;
  --brand:#1f8ad9;
  --brand-dark:#146bb0;
  --ink:#4a4f55;
  --muted:#9aa0a6;
}
*{margin:0;padding:0;box-sizing:border-box}
html,body{width:1200px;height:228px;overflow:hidden;background:var(--stage);font-family:'Montserrat',sans-serif;color:var(--ink)}
.stage{position:relative;width:1200px;height:228px}
.piece{position:absolute;background:var(--paper);overflow:hidden}
.brand{display:flex;align-items:center;gap:3px;color:var(--brand);font-weight:700;white-space:nowrap}
.brand .mark{background:var(--brand);display:block;flex:none}
.band{position:absolute;left:0;right:0;background:var(--brand)}
.tiny{font-size:3px;line-height:4.5px;color:var(--muted);white-space:nowrap}

/* business cards */
.card{width:56px;height:32px}
.card--front{background:var(--brand);display:flex;align-items:center;justify-content:center}
.card--front .brand{color:#fff;font-size:5px}
.card--front .mark{width:6px;height:6px;background:#fff}
.card--back{padding:4px}
.card--back .brand{font-size:4px}
.card--back .mark{width:5px;height:5px}
.card--back .band{bottom:0;height:3px}

/* vertical card */
.card--tall{width:28px;height:48px;background:var(--brand);display:flex;align-items:center;justify-content:center}
.card--tall .mark{width:10px;height:10px;background:#fff}

/* letterhead */
.letter{width:118px;height:168px;padding:10px}
.letter .brand{font-size:6px;justify-content:flex-end}
.letter .mark{width:8px;height:8px}
.letter .band{bottom:0;height:5px}
.letter .foot{position:absolute;bottom:9px;left:4px;right:4px;text-align:center;white-space:normal}

/* envelopes */
.envelope{width:128px;height:56px;padding:6px}
.envelope .brand{font-size:5px}
.envelope .mark{width:6px;height:6px}
.envelope .band{bottom:0;height:8px}
.envelope--back{background:var(--brand)}
.envelope--back svg{position:absolute;inset:0}

/* compliment slip */
.slip{width:70px;height:40px;padding:5px}
.slip .brand{font-size:4.5px}
.slip .mark{width:5px;height:5px}
.slip .band{bottom:0;height:4px}

/* disc */
.disc{width:78px;height:78px;border-radius:50%;background:var(--brand);display:flex;align-items:center;justify-content:center}
.disc .hub{width:18px;height:18px;border-radius:50%;background:var(--stage);border:4px solid #dfe6ec}
.disc .brand{position:absolute;top:16px;left:0;right:0;justify-content:center;color:#fff;font-size:5px}
.disc .mark{width:5px;height:5px;background:#fff}

/* pencil */
.pencil{position:absolute;height:4px;width:84px;background:var(--brand);transform:rotate(-30deg);border-radius:1px}

/* folder */
.folder{width:128px;height:176px;padding:10px}
.folder .brand{font-size:6px}
.folder .mark{width:8px;height:8px}
.folder .pocket{position:absolute;left:0;right:0;bottom:0;height:44px;background:var(--brand)}
.folder--inside{background:#f3f6f9}
.folder--inside .pocket{height:60px;border-top-right-radius:30px}
</style>
</head>
<body>
<main class="stage">

  <div class="piece card--tall" style="left:10px;top:40px"><span class="mark"></span></div>
  <div class="piece card card--front" style="left:44px;top:28px"><div class="brand"><span class="mark"></span>Quorvant Power</div></div>
  <div class="piece card card--back" style="left:44px;top:68px">
    <div class="brand"><span class="mark"></span>Quorvant Power</div>
    <p class="tiny" style="margin-top:3px">Derek Stallworth · President<br>derek@quorvantpower.example</p>
    <span class="band"></span>
  </div>
  <div class="piece card card--front" style="left:44px;top:108px"><div class="brand"><span class="mark"></span>Quorvant Power</div></div>
  <div class="piece card card--back" style="left:44px;top:148px">
    <div class="brand"><span class="mark"></span>Quorvant Power</div>
    <p class="tiny" style="margin-top:3px">48306 Calloway Avenue<br>720-555-0188</p>
    <span class="band"></span>
  </div>

  <div class="piece letter" style="left:124px;top:30px">
    <div class="brand"><span class="mark"></span>Quorvant Power</div>
    <p class="tiny foot">48306 Calloway Avenue · Fenmoor City, ST 00000<br>quorvantpower.example</p>
    <span class="band"></span>
  </div>
  <div class="piece letter" style="left:252px;top:30px">
    <div class="brand"><span class="mark"></span>Quorvant Power</div>
    <p class="tiny foot">720-555-0188 · derek@quorvantpower.example</p>
    <span class="band"></span>
  </div>

  <div class="piece envelope envelope--back" style="left:386px;top:30px">
    <svg viewBox="0 0 128 56" width="128" height="56"><path d="M0 0 L64 32 L128 0" fill="none" stroke="#fff" stroke-width="1.5"/></svg>
  </div>
  <div class="piece envelope" style="left:386px;top:96px">
    <div class="brand"><span class="mark"></span>Quorvant Power</div>
    <p class="tiny" style="margin-top:2px">48306 Calloway Avenue</p>
    <span class="band"></span>
  </div>
  <div class="piece envelope" style="left:386px;top:162px;height:50px">
    <div class="brand"><span class="mark"></span>Quorvant Power</div>
    <span class="band"></span>
  </div>

  <div class="piece slip" style="left:526px;top:96px">
    <div class="brand"><span class="mark"></span>Quorvant Power</div>
    <p class="tiny" style="margin-top:3px">With compliments</p>
    <span class="band"></span>
  </div>
  <div class="piece slip" style="left:526px;top:144px">
    <div class="brand"><span class="mark"></span>Quorvant Power</div>
    <p class="tiny" style="margin-top:3px">quorvantpower.example</p>
    <span class="band"></span>
  </div>

  <div class="piece disc" style="left:610px;top:110px">
    <div class="brand"><span class="mark"></span>Quorvant Power</div>
    <span class="hub"></span>
  </div>
  <span class="pencil" style="left:700px;top:70px"></span>

  <div class="piece folder" style="left:790px;top:26px">
    <div class="brand"><span class="mark"></span>Quorvant Power</div>
    <span class="pocket"></span>
  </div>
  <div class="piece folder folder--inside" style="left:924px;top:26px">
    <span class="pocket"></span>
  </div>
  <div class="piece folder" style="left:1058px;top:26px">
    <div class="brand"><span class="mark"></span>Quorvant Power</div>
    <p class="tiny" style="margin-top:4px">48306 Calloway Avenue<br>Fenmoor City, ST 00000</p>
    <span class="pocket" style="height:20px"></span>
  </div>

</main>
</body>
</html>
```